Accounting Practice Business Card Design

I have a logo I am happy for you to use in the design of the Business Card.
You can edit and change colours as you please, I am not fixated on it.
I am looking for a modern and clean overall feel for the finished design.

The business is a small accounting practice who thrives on word of mouth referrals and this card will be given to all current and prospect clients.

Industry/Entity Type

Accountant

Contact Information for Business Card

Marcus Elwin
Level 5, 8 Corvale Ridge Road
ASHGROVE RISE VIC 3187
Phone: 9481 3057
Email: melwin@mrfaccountants.com.au
Web: www.mrfaccountants.com.au

Font styles to use
Serif
Sans Serif

Colors
0555a3
3277b5
85acd3
0393ce
33a6d7
85cae6
00a990
33b8a4
9bcb3c

Requirements
Must have
• "The end to your tax problems begin with us"
• "A referral from you is our greatest compliment"
Nice to have
• Modern clean professional

```html
<!DOCTYPE html>
<html lang="en">
<head>
<meta charset="utf-8">
<title>MRF Accountants – Business Card</title>
<link rel="stylesheet" href="https://fonts.googleapis.com/css2?family=Roboto:wght@400;500;700;900&display=swap">
<style>
  :root {
    --backdrop: #3b3b3d;
    --brand-blue: #0555a3;
    --deep-blue: #0a4d8f;
    --brand-green: #3f7d1c;
    --lime: #9bcb3c;
    --ink: #1b1b1b;
    --paper: #ffffff;
  }
  * { box-sizing: border-box; margin: 0; padding: 0; }
  html, body {
    width: 1200px; height: 1000px; overflow: hidden;
    background: var(--backdrop);
    font-family: "Roboto", Arial, sans-serif;
  }
  .canvas { position: relative; width: 1200px; height: 1000px; }

  .card {
    position: absolute; width: 720px; height: 410px;
    border-radius: 24px; overflow: hidden;
  }

  /* Back of card */
  .card--back { left: 240px; top: 60px; background: var(--brand-blue); }
  .back__brand {
    position: absolute; left: 0; right: 0; top: 118px;
    text-align: center; color: var(--paper); font-weight: 900;
  }
  .back__brand-initials { display: block; font-size: 104px; line-height: 1; letter-spacing: 6px; }
  .back__brand-word { display: block; font-size: 44px; line-height: 1.1; letter-spacing: 3px; }
  .back__rule {
    position: absolute; left: 150px; right: 150px; top: 292px;
    height: 1px; background: rgba(255,255,255,.7);
  }
  .back__tagline {
    position: absolute; left: 0; right: 0; top: 302px;
    text-align: center; color: var(--lime); font-size: 19px; letter-spacing: .6px;
  }

  /* Front of card */
  .card--front { left: 240px; top: 520px; background: var(--paper); }
  .front__waves { position: absolute; inset: 0; }
  .front__brand {
    position: absolute; left: 44px; top: 62px;
    color: var(--brand-blue); font-weight: 900;
  }
  .front__brand-initials { display: block; font-size: 96px; line-height: 1; letter-spacing: 5px; }
  .front__brand-word { display: block; font-size: 34px; line-height: 1.1; letter-spacing: 2px; }
  .front__divider {
    position: absolute; left: 368px; top: 62px; width: 2px; height: 150px;
    background: var(--brand-blue);
  }
  .contact { position: absolute; left: 388px; top: 60px; color: var(--ink); }
  .contact__name { color: var(--brand-green); font-size: 23px; font-weight: 700; margin-bottom: 6px; }
  .contact__row { display: flex; align-items: flex-start; gap: 8px; font-size: 15px; font-weight: 500; line-height: 1.35; }
  .contact__row + .contact__row { margin-top: 2px; }
  .contact__row--gap { margin-top: 12px !important; }
  .contact__icon { width: 14px; height: 14px; flex: none; margin-top: 3px; }
  .contact__web-name { color: var(--brand-blue); font-weight: 700; }
  .front__tagline {
    position: absolute; left: 150px; top: 340px;
    color: var(--paper); font-size: 17px; font-weight: 500;
  }
</style>
</head>
<body>
<main class="canvas">

  <section class="card card--back" aria-label="Card back">
    <div class="back__brand">
      <span class="back__brand-initials">MRF</span>
      <span class="back__brand-word">ACCOUNTANTS</span>
    </div>
    <div class="back__rule"></div>
    <p class="back__tagline">A referral from you is our greatest compliment</p>
  </section>

  <section class="card card--front" aria-label="Card front">
    <svg class="front__waves" viewBox="0 0 720 410" preserveAspectRatio="none" aria-hidden="true">
      <path d="M0,215 C180,300 420,345 720,350 L720,410 L0,410 Z" fill="var(--brand-blue)"/>
      <path d="M320,318 C470,330 610,330 720,300 L720,338 C600,352 460,345 320,318 Z" fill="var(--brand-green)"/>
      <path d="M320,318 C470,338 600,348 720,338 L720,344 C600,354 460,346 320,318 Z" fill="var(--paper)"/>
    </svg>

    <div class="front__brand">
      <span class="front__brand-initials">MRF</span>
      <span class="front__brand-word">ACCOUNTANTS</span>
    </div>
    <div class="front__divider"></div>

    <div class="contact">
      <p class="contact__name">Marcus Elwin</p>
      <p class="contact__row">
        <svg class="contact__icon" viewBox="0 0 14 14" aria-hidden="true"><path d="M7 1a4 4 0 0 0-4 4c0 3 4 8 4 8s4-5 4-8a4 4 0 0 0-4-4zm0 5.5A1.5 1.5 0 1 1 7 3.5a1.5 1.5 0 0 1 0 3z" fill="var(--brand-green)"/></svg>
        <span>Level 5, 8 Corvale Ridge Road<br>ASHGROVE RISE VIC 3187</span>
      </p>
      <p class="contact__row contact__row--gap">
        <svg class="contact__icon" viewBox="0 0 14 14" aria-hidden="true"><path d="M3 1l2 0 1 3-1.5 1a7 7 0 0 0 4.5 4.5L10 8l3 1v2c0 1-1 2-2 2C6 13 1 8 1 3c0-1 1-2 2-2z" fill="var(--brand-green)"/></svg>
        <span>9481 3057</span>
      </p>
      <p class="contact__row">
        <svg class="contact__icon" viewBox="0 0 14 14" aria-hidden="true"><rect x="1" y="3" width="12" height="9" rx="1" fill="var(--brand-green)"/><path d="M1.5 3.5 7 8l5.5-4.5" stroke="#fff" stroke-width="1.2" fill="none"/></svg>
        <span>melwin@mrfaccountants.com.au</span>
      </p>
      <p class="contact__row">
        <svg class="contact__icon" viewBox="0 0 14 14" aria-hidden="true"><circle cx="7" cy="7" r="6" fill="var(--brand-green)"/><path d="M1 7h12M7 1c-2.5 3-2.5 9 0 12M7 1c2.5 3 2.5 9 0 12" stroke="#fff" stroke-width=".9" fill="none"/></svg>
        <span>www.<span class="contact__web-name">mrfaccountants</span>.com.au</span>
      </p>
    </div>

    <p class="front__tagline">The end to your tax problems begin with us</p>
  </section>

</main>
</body>
</html>
```